Corvello Paintless Dent Removal

Our company works on vehicles removing dents using a highly skilled trade which the metal is massaged out with special tools without disturbing the original paint, hence paintless dent removal. Besides keeping the paint and metal original its also very environmentally friendly since no paint or toxic fillers are used. Also we we are one of the most experienced companies in the business with 25 years

Target Market(s)

Retail Automobile consumers, Auto Dealerships and Auto Body Shops

Industry/Entity Type

Auto Repair

Contact Information for Business Card

Dwight Halvorsen
PO Box 538 Ashbrook, NY 11892
631-472-8169
corvellopdr@mailnest.example
website corvellopdr.example
youtube corvello paintless dent removal
25 years of experience removing Dents, Dings and Hail Damage

Font styles to use
Serif
Sans Serif

Colors

Designer to choose colors to be used in the design.

Requirements
Must have
• I do like things that are simple but classy and somewhat bold, also I like my logo so that should be somewhat important

```html
<!DOCTYPE html>
<html lang="en">
<head>
<meta charset="utf-8">
<title>Corvello Paintless Dent Removal — Business Card</title>
<link rel="stylesheet" href="https://fonts.googleapis.com/css2?family=Noto+Sans:wght@400;700&display=swap">
<style>
  :root {
    --navy: #13214a;
    --green: #5cb94a;
    --white: #ffffff;
    --backdrop: #e9e6e1;
    --card-shadow: rgba(19, 33, 74, 0.18);
  }
  html, body {
    margin: 0;
    width: 1200px;
    height: 800px;
    overflow: hidden;
    background: var(--backdrop);
    font-family: "Noto Sans", Verdana, sans-serif;
  }
  .card {
    position: absolute;
    left: 110px;
    top: 120px;
    width: 980px;
    height: 560px;
    background: var(--white);
    box-shadow: 0 14px 40px var(--card-shadow);
    overflow: hidden;
  }
  .card-art {
    position: absolute;
    inset: 0;
  }
  .brand {
    position: absolute;
    left: 600px;
    top: 96px;
    display: flex;
    align-items: center;
    gap: 14px;
    color: var(--navy);
    font-weight: 700;
  }
  .brand-dot {
    width: 40px;
    height: 40px;
    border-radius: 50%;
    background: var(--green);
    flex: none;
  }
  .brand-name {
    line-height: 1.05;
  }
  .brand-name .word {
    display: block;
    font-size: 48px;
    letter-spacing: 0.5px;
  }
  .brand-name .line {
    display: block;
    font-size: 19px;
  }
  .contact {
    position: absolute;
    left: 62px;
    top: 92px;
    color: var(--white);
  }
  .holder {
    margin: 0 0 22px;
    font-size: 36px;
    font-weight: 700;
    letter-spacing: 1px;
    text-transform: uppercase;
  }
  .holder .surname { color: var(--green); }
  .address {
    margin: 0 0 26px;
    font-size: 25px;
    line-height: 1.3;
  }
  .details {
    list-style: none;
    margin: 0 0 26px;
    padding: 0;
    font-size: 24px;
    line-height: 1.35;
  }
  .details li {
    display: flex;
    align-items: center;
    gap: 12px;
  }
  .details svg {
    width: 18px;
    height: 18px;
    fill: var(--green);
    flex: none;
  }
  .tagline {
    margin: 0;
    font-size: 25px;
    line-height: 1.3;
  }
  .tagline .services { display: block; color: var(--green); }
</style>
</head>
<body>
<div class="card">
  <svg class="card-art" viewBox="0 0 980 560" width="980" height="560" aria-hidden="true">
    <polygon points="0,0 470,0 690,300 980,300 980,560 0,560" fill="var(--navy)"/>
    <polygon points="0,452 840,528 820,548 0,494" fill="var(--green)"/>
    <polygon points="820,548 840,528 980,540 980,560 830,560" fill="var(--green)"/>
    <circle cx="980" cy="440" r="96" fill="var(--white)"/>
    <g class="social-row" fill="var(--white)">
      <circle cx="712" cy="332" r="15"/>
      <polygon points="740,322 860,318 852,334 740,338"/>
      <circle cx="745" cy="400" r="15"/>
      <polygon points="773,386 870,382 862,398 773,402"/>
      <circle cx="772" cy="466" r="15"/>
    </g>
  </svg>

  <div class="brand">
    <span class="brand-dot"></span>
    <span class="brand-name">
      <span class="word">CORVELLO</span>
      <span class="line">Paintless Dent Removal</span>
    </span>
  </div>

  <div class="contact">
    <h1 class="holder">Dwight <span class="surname">Halvorsen</span></h1>
    <p class="address">PO Box 538 Ashbrook<br>NY 11892</p>
    <ul class="details">
      <li><svg viewBox="0 0 24 24"><path d="M6.6 10.8a15.1 15.1 0 0 0 6.6 6.6l2.2-2.2c.3-.3.7-.4 1-.2 1.1.4 2.3.6 3.6.6.6 0 1 .4 1 1V20c0 .6-.4 1-1 1A17 17 0 0 1 3 4c0-.6.4-1 1-1h3.5c.6 0 1 .4 1 1 0 1.3.2 2.5.6 3.6.1.3 0 .7-.2 1z"/></svg>631-472-8169</li>
      <li><svg viewBox="0 0 24 24"><path d="M2 5h20v14H2z M4 7v.4l8 5.1 8-5.1V7z" fill-rule="evenodd"/></svg>corvellopdr@mailnest.example</li>
      <li><svg viewBox="0 0 24 24"><path d="M12 2a10 10 0 1 0 0 20 10 10 0 0 0 0-20zm6.9 6h-3a15.6 15.6 0 0 0-1.3-3.9A8 8 0 0 1 18.9 8zM12 4c.8 1.2 1.5 2.5 1.9 4h-3.8c.4-1.5 1.1-2.8 1.9-4zM4.3 14a8 8 0 0 1 0-4h3.4a16 16 0 0 0 0 4zm.8 2h3a15.6 15.6 0 0 0 1.3 3.9A8 8 0 0 1 5.1 16zm3-8h-3a8 8 0 0 1 4.3-3.9C8.8 5.3 8.4 6.6 8.1 8zM12 20c-.8-1.2-1.5-2.5-1.9-4h3.8c-.4 1.5-1.1 2.8-1.9 4zm2.3-6H9.7a14.7 14.7 0 0 1 0-4h4.6a14.7 14.7 0 0 1 0 4zm.3 5.9c.6-1.2 1-2.5 1.3-3.9h3a8 8 0 0 1-4.3 3.9zm1.7-5.9a16 16 0 0 0 0-4h3.4a8 8 0 0 1 0 4z"/></svg>www.corvellopdr.example</li>
    </ul>
    <p class="tagline">25 years of experience removing<span class="services">Dents, Dings and Hail Damage</span></p>
  </div>
</div>
</body>
</html>
```